Wordpress website design for Pelix Bridge-Africa

We need a website for a new consultancy and digital marketplace in Kenya called 'Pelix Bridge - Africa'. Please refer to the the attached document [Pelix Bridge Africa website brief] and contact me anytime.

Bests,
Rosalind
Updates

Deadline extended to allow for additional revisions and refinements, ensuring that final designs align closely with project objectives and quality standards. This extra time will help incorporate valuable feedback and ensure the final output meets our high expectations.

Coding

```html
<!DOCTYPE html>
<html lang="en">
<head>
<meta charset="utf-8">
<title>Pelix Bridge Africa</title>
<link rel="stylesheet" href="https://fonts.googleapis.com/css2?family=Inter:wght@400;500;600;700;800&display=swap">
<style>
:root{
  --blue:#0a45f0;
  --sky:#05b4f5;
  --ink:#1d2127;
  --text:#5b6068;
  --green:#8bc900;
  --green-dark:#5e9a00;
  --navy:#06129a;
  --lime:#9ad600;
  --white:#ffffff;
  --line:#e3e6ec;
}
*{margin:0;padding:0;box-sizing:border-box}
html,body{width:1200px;height:584px;overflow:hidden;background:var(--white)}
body{font-family:'Inter',sans-serif;color:var(--ink);position:relative}
.topbar{position:absolute;left:0;top:0;width:1200px;height:24px;background:linear-gradient(90deg,#0a3cf0,#0a7af4 55%,#05b8f5)}
.topbar__icon{position:absolute;left:242px;top:0;width:34px;height:24px;background:#0733c8;display:flex;align-items:center;justify-content:center}
.topbar__msg{position:absolute;left:285px;top:6px;font-size:8px;color:var(--white);letter-spacing:-.1px}
.topbar__msg b{font-weight:700}
.topbar__msg span{color:#9fd8ff;text-decoration:underline}
.topbar__social{position:absolute;left:830px;top:7px;display:flex;gap:13px}
.topbar__social i{display:block;width:9px;height:9px;border-radius:50%;background:var(--white)}
.header .logo{position:absolute;left:242px;top:44px;display:flex;align-items:center;gap:5px}
.logo__mark{width:14px;height:14px;border-radius:50%;background:var(--blue)}
.logo__name{font-size:14px;font-weight:700;color:var(--ink);letter-spacing:-.3px}
.nav{position:absolute;top:49px;left:339px;font-size:8px;font-weight:600;letter-spacing:.8px}
.nav a{position:absolute;white-space:nowrap;color:var(--ink);text-decoration:none}
.hotline{position:absolute;left:674px;top:40px;display:flex;align-items:center;gap:7px}
.hotline__icon{width:26px;height:26px;border-radius:50%;background:linear-gradient(135deg,var(--blue),var(--sky));display:flex;align-items:center;justify-content:center}
.hotline__label{font-size:8px;color:var(--text)}
.hotline__number{font-size:10px;font-weight:600;margin-top:3px}
.divider{position:absolute;left:817px;top:40px;width:1px;height:30px;background:var(--line)}
.search{position:absolute;left:831px;top:50px}
.btn-market{position:absolute;left:856px;top:44px;width:77px;height:23px;background:linear-gradient(90deg,var(--blue),#1a6ff5);color:var(--white);font-size:8px;font-weight:600;display:flex;align-items:center;justify-content:center}
.circuit{position:absolute;border-radius:50%;filter:blur(6px)}
.circuit--left{left:-40px;top:165px;width:230px;height:230px;background:radial-gradient(closest-side,rgba(120,180,250,.18),rgba(120,180,250,0))}
.circuit--right{left:600px;top:90px;width:620px;height:440px;background:radial-gradient(closest-side,rgba(90,170,250,.2),rgba(90,170,250,0))}
.hero{position:absolute;left:311px;top:150px;width:300px}
.hero__eyebrow{font-size:9px;font-weight:600;color:var(--green);letter-spacing:.1px}
.hero__title{margin-top:8px;font-size:29px;font-weight:700;line-height:34px;letter-spacing:.2px}
.hero__sub{font-size:20px;font-weight:400;line-height:21px;margin-top:1px}
.hero__text{margin-top:14px;font-size:10.3px;line-height:16px;color:var(--text);width:260px;letter-spacing:.1px}
.btn-services{position:absolute;left:311px;top:383px;width:86px;height:29px;background:var(--ink);color:var(--white);border-radius:2px;font-size:10px;display:flex;align-items:center;justify-content:center}
.intro{position:absolute;left:414px;top:382px;display:flex;align-items:center;gap:8px}
.intro__play{width:30px;height:30px;border-radius:50%;background:#e4eef8;display:flex;align-items:center;justify-content:center}
.intro__play span{width:20px;height:20px;border-radius:50%;background:var(--green);display:flex;align-items:center;justify-content:center}
.intro__label{font-size:8px;font-weight:700;color:var(--green-dark);line-height:11px}
.hero__media{position:absolute;left:642px;top:141px;width:282px;height:285px}
.partners{position:absolute;left:242px;top:506px;width:721px;height:78px;border-radius:5px 5px 0 0;background:linear-gradient(90deg,var(--navy),#3c5a5e 45%,var(--lime))}
.partners__name{position:absolute;top:47px;transform:translateY(-50%);font-size:13px;font-weight:600;color:var(--white);white-space:nowrap}
</style>
</head>
<body>
<div class="topbar">
  <div class="topbar__icon">
    <svg width="11" height="10" viewBox="0 0 11 10"><path d="M1 3.5h2.5L8 1v8L3.5 6.5H1z" fill="#fff"/><path d="M3 6.5l1 3h1.4l-1-3z" fill="#fff"/></svg>
  </div>
  <p class="topbar__msg"><b>Join us:</b> Let's revolutionize Africa's <span>Digital future</span></p>
  <div class="topbar__social" aria-label="Social links"><i></i><i></i><i></i><i></i></div>
</div>

<header class="header">
  <div class="logo"><span class="logo__mark"></span><span class="logo__name">Pelix</span></div>
  <nav class="nav">
    <a style="left:0">Home</a>
    <a style="left:49px">Services</a>
    <a style="left:112px">Shop</a>
    <a style="left:159px">About</a>
    <a style="left:210px">Blog</a>
    <a style="left:254px">Contact</a>
  </nav>
  <div class="hotline">
    <div class="hotline__icon">
      <svg width="11" height="11" viewBox="0 0 24 24"><path d="M6.6 10.8a15 15 0 0 0 6.6 6.6l2.2-2.2a1 1 0 0 1 1-.25 11.4 11.4 0 0 0 3.6.57 1 1 0 0 1 1 1V20a1 1 0 0 1-1 1A17 17 0 0 1 3 4a1 1 0 0 1 1-1h3.5a1 1 0 0 1 1 1c0 1.25.2 2.45.57 3.57a1 1 0 0 1-.25 1z" fill="none" stroke="#fff" stroke-width="1.6"/></svg>
    </div>
    <div>
      <p class="hotline__label">hotline 24/7</p>
      <p class="hotline__number">(+254) 700 555 0123</p>
    </div>
  </div>
  <div class="divider"></div>
  <svg class="search" width="11" height="11" viewBox="0 0 12 12"><circle cx="5" cy="5" r="4" fill="none" stroke="#1d2127" stroke-width="1.2"/><path d="M8 8l3 3" stroke="#1d2127" stroke-width="1.2"/></svg>
  <div class="btn-market">Marketplace</div>
</header>

<div class="circuit circuit--left" role="img" aria-label="Faint circuit-line decoration"></div>
<div class="circuit circuit--right" role="img" aria-label="Faint circuit-line decoration"></div>

<section class="hero">
  <p class="hero__eyebrow">PELIX BRIDGE AFRICA</p>
  <h1 class="hero__title">Empowering<br>Innovations</h1>
  <p class="hero__sub">&amp; Digital Transformation<br>Across Africa."</p>
  <p class="hero__text">We provide data-driven insights, strategic guidance, customised solutions to empower public and private sectors</p>
</section>
<div class="btn-services">our services</div>
<div class="intro">
  <div class="intro__play"><span><svg width="8" height="8" viewBox="0 0 8 8"><path d="M2 1l5 3-5 3z" fill="none" stroke="#fff" stroke-width="1"/></svg></span></div>
  <p class="intro__label">Intro<br>Reel</p>
</div>

<svg class="hero__media" viewBox="0 0 282 285" role="img" aria-label="Photo of a team of young professionals gathered around a laptop">
  <defs>
    <linearGradient id="blobEdge" x1="0" y1="0" x2="1" y2="1"><stop offset="0" stop-color="#0a45f0"/><stop offset="1" stop-color="#05b4f5"/></linearGradient>
    <linearGradient id="photoTone" x1="0" y1="0" x2="0" y2="1"><stop offset="0" stop-color="#e8e8ec"/><stop offset=".55" stop-color="#8a7668"/><stop offset="1" stop-color="#3a302c"/></linearGradient>
  </defs>
  <path d="M90 14C60 26 20 60 8 110 -2 160 8 220 50 255 90 285 170 290 220 265 262 242 285 190 280 140 276 90 250 40 200 18 160 2 120 2 90 14z" fill="url(#blobEdge)"/>
  <circle cx="142" cy="141" r="138" fill="url(#photoTone)"/>
</svg>

<section class="partners">
  <span class="partners__name" style="left:76px">Newsferry</span>
  <span class="partners__name" style="left:207px">Open Field</span>
  <span class="partners__name" style="left:336px">Bytewell</span>
  <span class="partners__name" style="left:434px">Quenlo</span>
  <span class="partners__name" style="left:573px">Morvane</span>
</section>
</body>
</html>
```